Consulting company needs website design

We need a simple, static website design for our consulting company. We are looking for a general design of the look and feel of the website. Initially, it will have these pages:
- Home
- About us
- Services
- Contact us
We have our own logo which I have attached to the brief.

We are looking for a simple website, with white background and the use of gray (darker) as the main theme. Simple fonts. The website should be responsive so it an be easily red in mobile devices.

As part of the project, we will need to receive at least the following items:
- Individual files with sample text to support the pages outlined above
- Necessary CSS files

Our current website is here: http://www.marlowvane.co/

Here are some examples of other website we like to be used as guideline:
- http://www.tornaviamundo.com/
-

Target Market(s)

Individuals and companies looking to hire our company to provide consulting services.

Industry/Entity Type

It Company

Coding

Coded - Design and coding required

Number of Pages Required

4 page

Font styles to use
Sans Serif

Requirements
Must have
• Main page should have the ability to embed Chirply feed into it.
• We prefer the design to use gray tones.

```html
<!DOCTYPE html>
<html lang="en">
<head>
<meta charset="utf-8">
<title>Marlow Vane — Consulting</title>
<link rel="stylesheet" href="https://fonts.googleapis.com/css2?family=Open+Sans:wght@400;600;700&family=Questrial&display=swap">
<style>
:root{
  --ink:#222;
  --text:#555;
  --muted:#8a8a8a;
  --dark:#2f2f2f;
  --darker:#262626;
  --footer:#2b2b2b;
  --bar:#1f1f1f;
  --line:#d9d9d9;
  --soft:#e8e8e8;
  --pale:#f4f4f4;
  --white:#fff;
  --icon:#3d3d3d;
}
*{box-sizing:border-box;margin:0;padding:0}
html,body{width:1200px;height:3130px;overflow:hidden}
body{position:relative;background:var(--white);font-family:"Open Sans",Arial,sans-serif;color:var(--text);font-size:13px}
.heading{font-family:"Questrial","Century Gothic",sans-serif;color:var(--ink);font-weight:400}
section,header,footer{position:absolute;left:0;width:1200px}

/* top bar */
.topbar{top:0;height:34px;background:var(--dark);color:#cfcfcf;font-size:11px;display:flex;align-items:center;padding:0 60px;gap:22px}
.topbar .social{margin-left:auto;display:flex;gap:14px}
.topbar svg{width:11px;height:11px;fill:#cfcfcf;vertical-align:-1px;margin-right:5px}

/* header */
.site-header{top:34px;height:112px;background:var(--white)}
.brand{position:absolute;left:58px;top:20px;width:150px;height:150px;border-radius:50%;background:var(--white);border:3px solid var(--soft);display:flex;align-items:center;justify-content:center;z-index:3;font-family:"Questrial",sans-serif;font-size:20px;color:var(--ink);text-align:center;line-height:1.2}
.contact-line{position:absolute;left:222px;top:26px;display:flex;gap:26px;font-size:13px;color:var(--ink)}
.contact-line svg{width:16px;height:16px;fill:none;stroke:var(--ink);stroke-width:1.6;vertical-align:-3px;margin-right:6px}
.cta{position:absolute;right:60px;top:12px;background:#6b6b6b;color:var(--white);font-size:11px;font-weight:700;padding:11px 16px}
.nav{position:absolute;left:232px;top:76px;display:flex;gap:27px;font-size:13px;font-weight:700;color:var(--ink);letter-spacing:.3px}
.search{position:absolute;right:60px;top:66px;width:40px;height:34px;background:#d6d6d6;display:flex;align-items:center;justify-content:center}
.search svg{width:17px;height:17px;stroke:#333;stroke-width:2;fill:none}

/* hero */
.hero{top:146px;height:434px;background:linear-gradient(100deg,#b9a389 0%,#7b6a58 40%,#5f564c 65%,#a59885 100%)}
.welcome{position:absolute;left:605px;top:167px;width:537px;height:142px;background:rgba(30,30,30,.82);padding:26px 22px;color:var(--white)}
.welcome h1{font-family:"Questrial",sans-serif;font-weight:400;font-size:42px;line-height:1.1}
.welcome p{font-size:16px;margin-top:10px;padding-left:24px;color:#e6e6e6}

/* services */
.services{top:580px;height:597px}
.section-title{text-align:center;font-size:38px;padding-top:22px}
.rule{width:48px;height:2px;background:var(--ink);margin:14px auto 0}
.service-grid{position:absolute;top:92px;left:60px;width:1080px;display:grid;grid-template-columns:repeat(3,300px);justify-content:space-between;row-gap:4px}
.service{height:242px;text-align:center;padding:18px 10px 0}
.service:nth-child(n+4){height:190px}
.service.is-active{background:var(--soft)}
.service .icon{width:66px;height:66px;border-radius:50%;background:var(--icon);margin:0 auto;display:flex;align-items:center;justify-content:center}
.service .icon svg{width:30px;height:30px;stroke:var(--white);fill:none;stroke-width:1.8}
.service h3{font-size:17px;font-weight:700;color:var(--ink);margin-top:14px;letter-spacing:.4px}
.service p{font-size:12px;line-height:1.85;margin-top:4px}
.btn-small{display:inline-block;background:var(--icon);color:var(--white);font-size:11px;font-weight:700;padding:8px 14px;margin-top:10px}

/* about */
.about{top:1177px;height:413px;background:var(--dark)}
.about-photo{position:absolute;left:58px;top:-50px;width:652px;height:463px;border-radius:0 0 46% 0 / 0 0 30% 0;background:radial-gradient(ellipse at 50% 45%,#c9b3a0 0%,#8d7d72 55%,#4b4643 100%)}
.about-body{position:absolute;left:750px;top:62px;width:390px;color:#e6e6e6}
.about-body h2{font-size:38px;color:var(--white)}
.about-body p{font-size:12px;line-height:1.9;margin-top:18px}
.btn-light{display:inline-block;background:var(--white);color:var(--ink);font-weight:700;font-size:14px;padding:12px 32px;margin-top:28px}
.btn-light svg{width:8px;height:9px;fill:var(--ink);margin-left:5px}

/* testimonials */
.clients{top:1590px;height:501px;text-align:center}
.clients .section-title{padding-top:64px}
.quote{width:940px;margin:36px auto 0;font-size:12px;line-height:1.95}
.client-name{font-family:"Questrial",sans-serif;font-size:19px;font-weight:700;color:#666;margin-top:34px}
.avatars{position:relative;width:170px;height:110px;margin:16px auto 0}
.hex{position:absolute;width:52px;height:58px;clip-path:polygon(50% 0,100% 25%,100% 75%,50% 100%,0 75%,0 25%)}

/* find adviser */
.adviser{top:2091px;height:522px;background:linear-gradient(180deg,#8d8a86 0%,#a7a39e 45%,#6f6c69 100%)}
.adviser-card{position:absolute;left:60px;top:94px;width:1080px;height:340px;background:var(--white);padding:52px 54px}
.adviser-card h2{font-size:38px}
.adviser-intro{width:390px;font-size:12px;line-height:1.85;margin-top:22px}
.hours{font-size:12px;font-weight:700;color:#444;line-height:1.9;margin-top:18px}
.form{position:absolute;left:478px;top:40px;width:526px;display:grid;grid-template-columns:1fr 1fr;gap:10px 12px}
.field{height:44px;border:1px solid var(--line);color:#999;font-size:13px;display:flex;align-items:center;justify-content:center}
.field.wide{grid-column:1/3;height:98px;align-items:flex-start;padding-top:14px}
.submit{grid-column:1/3;height:42px;background:var(--dark);color:var(--white);font-weight:700;font-size:13px;display:flex;align-items:center;justify-content:center;margin-top:2px}

/* partners */
.partners{top:2613px;height:163px;background:var(--pale);display:flex;align-items:center;justify-content:space-around;padding:0 60px}
.partner{display:flex;flex-direction:column;align-items:center;gap:8px;font-size:15px;font-weight:600;color:#a3a3a3}
.partner i{width:40px;height:40px;border-radius:50%;background:#bdbdbd;display:block}

/* footer */
.site-footer{top:2776px;height:309px;background:var(--footer);color:#9a9a9a;font-size:12px}
.col{position:absolute;top:44px}
.col h4{font-family:"Questrial",sans-serif;font-size:20px;color:var(--white);font-weight:700}
.col-contact{left:60px;width:340px}
.col-contact p{line-height:1.8;margin-top:20px}
.col-contact ul{list-style:none;margin-top:10px}
.col-contact li{margin-top:12px;color:#bbb}
.col-contact svg{width:12px;height:12px;fill:#aaa;margin-right:10px;vertical-align:-1px}
.col-explore{left:484px}
.links{display:grid;grid-template-columns:120px 120px;row-gap:15px;margin-top:26px;color:#ddd;font-size:12px}
.col-subscribe{left:807px;width:333px}
.subscribe{display:flex;margin-top:24px}
.subscribe .input{flex:1;height:40px;background:var(--white)}
.subscribe .send{width:56px;height:40px;background:#8a8a8a;display:flex;align-items:center;justify-content:center}
.subscribe svg{width:18px;height:14px;fill:var(--white)}
.note{margin-top:16px;padding-bottom:14px;border-bottom:1px solid #3d3d3d}
.socials{display:grid;grid-template-columns:135px 135px;row-gap:14px;margin-top:16px;color:#ddd}
.socials span::before{content:"";display:inline-block;width:8px;height:8px;border-radius:50%;background:#bbb;margin-right:10px}
.copyright{position:absolute;top:3085px;left:0;width:1200px;height:45px;background:var(--bar);color:#aaa;font-size:11px;display:flex;align-items:center;justify-content:center}
</style>
</head>
<body>

<header class="topbar">
  <span><svg viewBox="0 0 12 12"><path d="M6 1 1 5.5h1.5V11h7V5.5H11z"/></svg>2180 W. Linden Ave, Fairbrook</span>
  <span><svg viewBox="0 0 12 12"><circle cx="6" cy="6" r="5" fill="none" stroke="#cfcfcf" stroke-width="1.3"/><path d="M6 3v3.3l2 1.2" stroke="#cfcfcf" stroke-width="1.2" fill="none"/></svg>Mon - Sat: 7:00 - 17:00</span>
  <span class="social"><span>F</span><span>C</span><span>L</span></span>
</header>

<header class="site-header">
  <div class="brand">Marlow<br>Vane</div>
  <div class="contact-line">
    <span><svg viewBox="0 0 16 16"><path d="M4 2l2 3-1.5 1.5c1 2 3 4 5 5L11 10l3 2-1 2.5C7 14 2 9 1.5 3z"/></svg>(555) 014-2277</span>
    <span><svg viewBox="0 0 16 16"><rect x="1.5" y="3.5" width="13" height="9"/><path d="M1.5 3.5 8 9l6.5-5.5"/></svg>info@marlowvane.co</span>
  </div>
  <div class="cta">FREE CONSULTATION</div>
  <nav class="nav"><span>HOME</span><span>OUR FIRM</span><span>PRACTICE</span><span>AREAS</span><span>ATTORNEYS</span><span>BLOG</span><span>CONTACT</span></nav>
  <div class="search"><svg viewBox="0 0 18 18"><circle cx="7.5" cy="7.5" r="5.5"/><path d="M11.5 11.5 16 16"/></svg></div>
</header>

<section class="hero" role="img" aria-label="Photograph of a senior consultant in a suit with colleagues in an office">
  <div class="welcome">
    <h1>Welcome to our company</h1>
    <p>We bring value, innovation and growth to your business</p>
  </div>
</section>

<section class="services">
  <h2 class="section-title heading">Services</h2>
  <div class="rule"></div>
  <div class="service-grid">
    <div class="service is-active">
      <div class="icon"><svg viewBox="0 0 30 30"><rect x="5" y="5" width="20" height="20"/><path d="M10 21v-5M15 21v-8M20 21v-11"/></svg></div>
      <h3>LAWYER CONSULTING</h3>
      <p>There are many variations of passages of Lorem Ipsum available majority have suffered alter-ationmajority have suffered alteration .</p>
      <span class="btn-small">Read More</span>
    </div>
    <div class="service">
      <div class="icon"><svg viewBox="0 0 30 30"><circle cx="15" cy="11" r="5"/><path d="M6 25c1-6 5-8 9-8s8 2 9 8"/></svg></div>
      <h3>PERSONALITY</h3>
      <p>There are many variations of passages of Lorem Ipsum available majority have suffered alter-ationmajority have suffered alteration .</p>
    </div>
    <div class="service">
      <div class="icon"><svg viewBox="0 0 30 30"><rect x="5" y="6" width="20" height="14"/><path d="M11 24h8M15 20v4"/></svg></div>
      <h3>EXPERIENCED</h3>
      <p>There are many variations of passages of Lorem Ipsum available majority have suffered alter-ationmajority have suffered alteration .</p>
    </div>
    <div class="service">
      <div class="icon"><svg viewBox="0 0 30 30"><rect x="5" y="5" width="20" height="20"/><path d="M10 21v-5M15 21v-8M20 21v-11"/></svg></div>
      <h3>IT MANAGEMENT</h3>
      <p>There are many variations of passages of Lorem Ipsum available majority have suffered alter-ationmajority have suffered alteration .</p>
    </div>
    <div class="service">
      <div class="icon"><svg viewBox="0 0 30 30"><circle cx="16" cy="11" r="5"/><path d="M13 15l-6 10M10 20l4 2"/></svg></div>
      <h3>ONLINE CONSULTING</h3>
      <p>There are many variations of passages of Lorem Ipsum available majority have suffered alter-ationmajority have suffered alteration .</p>
    </div>
    <div class="service">
      <div class="icon"><svg viewBox="0 0 30 30"><rect x="5" y="5" width="20" height="20"/><path d="M10 21v-5M15 21v-8M20 21v-11"/></svg></div>
      <h3>BUSINESS CONSULTING</h3>
      <p>There are many variations of passages of Lorem Ipsum available majority have suffered alter-ationmajority have suffered alteration .</p>
    </div>
  </div>
</section>

<section class="about">
  <div class="about-photo" role="img" aria-label="Photograph of a cheerful group of business people giving thumbs up"></div>
  <div class="about-body">
    <h2 class="heading">About us</h2>
    <p>Marlow Vane is one of the world's leading financial consulting firms. We work with clients to help them have a thorough look about their financial situations, make better decisions, get those decisions translated quickly into actions and sustain the momen-tum into the future.</p>
    <span class="btn-light">Read More<svg viewBox="0 0 8 9"><path d="M0 0l8 4.5L0 9z"/></svg></span>
  </div>
</section>

<section class="clients">
  <h2 class="section-title heading">Happy Clients</h2>
  <div class="rule"></div>
  <p class="quote">Lorem Ipsum is simply dummy text of the printing and typesetting industry. Lorem Ipsum has been the industry's standard dummy text ever since the 1500s, when an unknown printer took a galley of type and scrambled it to make a type specimen book. It has survived not only five centuries, but also the leap into electronic typesetting, remaining essentially unchanged. It was popularised in the 1960s with the release of Letraset sheets.<br>plant-image</p>
  <div class="client-name">Tomas Averin</div>
  <div class="avatars">
    <div class="hex" role="img" aria-label="Client portrait" style="left:3px;top:0;background:#b49a86"></div>
    <div class="hex" role="img" aria-label="Client portrait" style="left:59px;top:0;background:#5a4a40"></div>
    <div class="hex" role="img" aria-label="Client portrait" style="left:115px;top:0;background:#a89a92"></div>
    <div class="hex" role="img" aria-label="Client portrait" style="left:31px;top:48px;background:#9b7f6d"></div>
    <div class="hex" role="img" aria-label="Client portrait" style="left:87px;top:48px;background:#c2ab98"></div>
  </div>
</section>

<section class="adviser" role="img" aria-label="Blurred photograph of advisers at a meeting table">
  <div class="adviser-card">
    <h2 class="heading">Find Adviser</h2>
    <p class="adviser-intro">Would you like to speak to one of our financial advisers over the phone? Just submit your details and we'll be in touch shortly. You can also e-mail us for any further concern.</p>
    <p class="hours">Monday to Friday : 8AM to 8PM<br>Sartuday : 9AM to 11AM<br>Sunday &amp; Holidays : Closed</p>
    <div class="form">
      <div class="field">Your Name</div>
      <div class="field">Your Email</div>
      <div class="field">Phone</div>
      <div class="field">Saving &amp; Investing</div>
      <div class="field wide">Other Details</div>
      <div class="submit">Find Your Advisor</div>
    </div>
  </div>
</section>

<section class="partners">
  <div class="partner"><i></i>Cellora</div>
  <div class="partner"><i></i>Vantor</div>
  <div class="partner"><i></i>Glimmer Media</div>
  <div class="partner"><i></i>Openroom</div>
  <div class="partner"><i></i>Highcrest</div>
  <div class="partner"><i></i>Glimmer Media</div>
</section>

<footer class="site-footer">
  <div class="col col-contact">
    <h4>Contact Us</h4>
    <p>Marlow Vane is one of the world's Leading financial consulting firms.</p>
    <ul>
      <li><svg viewBox="0 0 12 12"><path d="M6 0a4 4 0 0 0-4 4c0 3 4 8 4 8s4-5 4-8a4 4 0 0 0-4-4z"/></svg>36 Harrow Lane, Westbridge, Elmshire.</li>
      <li><svg viewBox="0 0 12 12"><path d="M2.5 1l2 2.5-1 1.2c.8 1.5 2 2.7 3.5 3.5l1.2-1L10.7 9 10 11C5 10.5 1.5 7 1 2z"/></svg>(555) 019-4410</li>
      <li><svg viewBox="0 0 12 12"><path d="M0 2h12v8H0z"/></svg>hello@marlowvane.co</li>
      <li><svg viewBox="0 0 12 12"><path d="M0 1h12v8H0zM4 10h4v1H4z"/></svg>www.marlowvane.co</li>
    </ul>
  </div>
  <div class="col col-explore">
    <h4>Explore</h4>
    <div class="links">
      <span>Home</span><span>About Us</span>
      <span>Service</span><span>Testimonials</span>
      <span>News</span><span>Contact Us</span>
      <span>Bonds</span><span>Commodities</span>
      <span>Investments</span><span>Retirement</span>
      <span>Stocks</span><span>Trends</span>
    </div>
  </div>
  <div class="col col-subscribe">
    <h4>Subscribe</h4>
    <div class="subscribe"><div class="input"></div><div class="send"><svg viewBox="0 0 18 14"><path d="M0 0h18v14H0zM1 1l8 6 8-6" stroke="#8a8a8a" stroke-width="1.2"/></svg></div></div>
    <p class="note">Get Latest updates and offers.</p>
    <div class="socials"><span>Facepage</span><span>Circlenet</span><span>Chirply</span><span>Linkroll</span></div>
  </div>
</footer>
<div class="copyright">© 2016 MARLOW VANE GROUP Right Reserved.</div>

</body>
</html>
```